載内容詳細に関しては、別添のExcel資料を参照してください。

・ターゲット
BtoB
木工架装を出来る業者を探している車のリース販売会社の担当様

・カラーイメージ
木目デザインと企業カラーである紺色を使用してデザインお願いします
▼木目参考
https://www.tomika-kobo.jp/
▼紺参考
https://www.rvm-t.jp/

・デザイン、ムード
木を扱う仕事なので、木目を上手く使ってデザインしてほしい
▼参考

・JQについて
JQのパターン制作は不要です。
1枚目の画像でデザインお願いします

配置やデザイン等はアレンジしていただいて構いません。
また、縦に制限はありません。

レスポンシブデザインのサイトで、bootstrap4を利用しコーディングする予定になります。

デザイン幅は2000px、コンテンツの幅はbootstrap4デフォルトのの1110pxを基準としてください。
ただし、最近のデザインの流行を取りいれて、フルワイドや、1200~15000px程度の幅のコンテンツをバランスよくレイアウトしてください。
コンテンツ配置は基本12分割になります。がデザインによっては、多少逸脱してもかまいません。
bootstrap4、12分割グリッドの基準のPSDも資料として添付しております。
ご参考になさってください。

本分のフォントはゴシック系は游ゴシック、メイリオ、明朝系は遊明朝でお願いします。
飾り文字はフリーフォントか、googleフォントを利用してください。

メイン画像部分・グローバルメニューは、ワイド適用でお願いします。

不明点、質問などありましたらメッセージ等でご連絡ください。
1ページ
青系、水色系
• 高解像度JPG (.jpg)
• フォトショップ形式 (.psd)
・資料上はサイト名(社名)や住所などは伏字にしております。
ご提案時点ではそのまま作成をお願いします。

・使用画像は当選後こちらで用意します。
ご提案時点では前項同様に、カンプデータ等をご使用のうえ、当選後に本内容へ差し替え修正をお願いします。
また、雰囲気が合っていれば、指定外の画像を追加掲載いただいてOKです。

・当選前提となった方は正式な社名及び連絡先をお伝えしますので修正対応をお願いします。
また希望の際は、当選後、中ページの制作及びコーディングも別途ご依頼可能です。

```html
<!DOCTYPE html>
<html lang="ja">
<head>
<meta charset="utf-8">
<title>清瀬木工架装株式会社</title>
<link rel="stylesheet" href="https://fonts.googleapis.com/css2?family=Noto+Sans+JP:wght@400;500;700;900&display=swap">
<style>
:root{
  --navy:#123f86;
  --navy-dark:#0d2c5e;
  --wood:#c8743a;
  --wood-light:#e29a5a;
  --wood-dark:#8a4a22;
  --text:#333;
  --white:#fff;
  --orange:#f0a040;
}
*{margin:0;padding:0;box-sizing:border-box}
html,body{width:735px;height:1200px;overflow:hidden;background:#fff}
body{font-family:"Noto Sans JP",sans-serif;color:var(--text);position:relative}
.abs{position:absolute}
/* hero */
.hero{left:0;top:0;width:735px;height:282px;background:linear-gradient(180deg,#2b2723 0%,#6b4a34 35%,#b9703a 70%,#d58848 100%)}
.hero-header{left:0;top:0;width:735px;height:46px;display:flex;align-items:center;padding:0 16px;color:var(--white)}
.brand{font-size:9px;font-weight:700;line-height:1.3;width:150px}
.brand small{display:block;font-weight:400;font-size:7px}
.gnav{display:flex;align-items:center;gap:22px;margin-left:110px;font-size:9px;font-weight:500}
.gnav .is-current{background:rgba(255,255,255,.9);color:var(--navy);padding:10px 8px}
.header-cta{margin-left:auto;background:var(--navy);font-size:9px;padding:7px 12px}
.hero-title{left:0;top:140px;width:735px;text-align:center;color:var(--white);font-size:27px;font-weight:900;line-height:1.3;text-shadow:0 2px 6px rgba(0,0,0,.6)}
/* intro */
.intro-heading{left:32px;top:300px;font-size:16px;font-weight:900;color:var(--navy);line-height:1.5}
.intro-heading::after{content:"";display:block;width:230px;height:2px;background:var(--navy);margin-top:6px}
.intro-text{left:32px;top:360px;width:300px;font-size:8px;line-height:1.75}
.intro-photo{left:360px;top:318px;width:350px;height:125px;background:linear-gradient(135deg,#3a3a3a,#b7713c 55%,#d99258)}
.intro-photo-label{left:372px;top:326px;color:var(--white);font-size:14px;font-weight:700;line-height:1.2;text-shadow:0 1px 4px rgba(0,0,0,.6)}
/* service */
.band{left:0;top:455px;width:735px;height:22px;background:var(--navy)}
.service{left:0;top:465px;width:735px;height:200px;background:linear-gradient(180deg,var(--wood-dark),var(--wood) 40%,var(--wood-light))}
.service-title{left:0;top:504px;width:735px;text-align:center;font-size:15px;font-weight:900;color:var(--orange);text-shadow:0 1px 3px rgba(0,0,0,.5)}
.service-text{left:0;top:540px;width:735px;text-align:center;font-size:8.5px;line-height:1.9;color:var(--white);text-shadow:0 1px 2px rgba(0,0,0,.5)}
.btn{background:var(--navy);color:var(--white);font-size:8px;text-align:center;display:flex;align-items:center;justify-content:center}
.service-btn{left:337px;top:624px;width:62px;height:22px}
/* works */
.works-title{left:0;top:690px;width:735px;text-align:center;font-size:16px;font-weight:900;color:var(--text)}
.works-item{background:linear-gradient(160deg,#444,#b8703a 60%,#dd945a)}
.works-1{left:147px;top:752px;width:110px;height:82px}
.works-2{left:265px;top:730px;width:205px;height:115px}
.works-3{left:478px;top:752px;width:110px;height:82px}
.works-btn{left:337px;top:866px;width:62px;height:22px}
/* contact */
.contact-bg{left:147px;top:915px;width:441px;height:185px;background:linear-gradient(90deg,#c07a45,#d69660)}
.contact-photo{left:147px;top:915px;width:294px;height:185px;background:linear-gradient(135deg,#5b4030,#a07858 50%,#c9a27e)}
.contact-panel{left:441px;top:915px;width:147px;height:185px;background:var(--navy);color:var(--white);padding:22px 16px;text-align:center}
.contact-panel h2{font-size:13px;font-weight:900;color:var(--orange)}
.contact-panel .en{font-size:8px;margin-bottom:18px}
.contact-panel .tel{font-size:9px;font-weight:700;margin-bottom:10px}
.contact-panel .btn{width:60px;height:20px;background:var(--white);color:var(--navy);margin:0 auto}
/* footer */
.footer{left:0;top:1112px;width:735px;height:88px;background:var(--navy-dark);color:var(--white);padding:24px 40px;display:flex}
.footer-info{font-size:8px;line-height:1.8}
.footer-info strong{font-size:9px}
.footer-nav{margin-left:auto;display:flex;gap:18px;font-size:8px;margin-right:40px;margin-top:2px}
.pagetop{right:24px;top:1132px;width:24px;height:24px;background:var(--navy)}
</style>
</head>
<body>
<section class="abs hero" role="img" aria-label="木製の床を架装した車の荷室の写真"></section>
<header class="abs hero-header">
  <div class="brand">清瀬木工架装株式会社<small>車内木工架装工事</small></div>
  <nav class="gnav"><span>ホーム</span><span class="is-current">業務内容</span><span>施工事例</span><span>会社概要</span></nav>
  <div class="header-cta">お問い合わせ</div>
</header>
<h1 class="abs hero-title">Kiyose<br>Woodworking</h1>

<h2 class="abs intro-heading">車内の木工架装工事なら<br>○○○○にご相談ください！</h2>
<p class="abs intro-text">“安心・確実”お客様のご要望に、確かな技術でお応えします。<br>○○○○は車内の木工架装工事を専門に手がけております。<br>長年培った技術と経験を活かし、一台一台丁寧に仕上げます。<br>床張り・棚の造作・内装パネルなど幅広く対応いたします。<br>リース車両の架装もお気軽にご相談ください。<br>お見積りは無料です。まずはお問い合わせください。</p>
<div class="abs intro-photo" role="img" aria-label="木製の床を張った車内の写真"></div>
<div class="abs intro-photo-label">Woodworking<br>in the car</div>

<div class="abs band"></div>
<section class="abs service" role="img" aria-label="木目の床の写真"></section>
<h2 class="abs service-title">業務内容</h2>
<p class="abs service-text">車の中を心地よい木の空間へと仕上げます。<br>商用車の荷室や内装の木工架装を幅広く手がけています。<br>ご要望に合わせた設計から施工まで一貫して対応します。<br>お気軽にご相談ください。</p>
<div class="abs btn service-btn">詳細はこちら</div>

<h2 class="abs works-title">施工事例</h2>
<div class="abs works-item works-1" role="img" aria-label="施工事例：車内の棚"></div>
<div class="abs works-item works-2" role="img" aria-label="施工事例：荷室の木製床"></div>
<div class="abs works-item works-3" role="img" aria-label="施工事例：内装パネル"></div>
<div class="abs btn works-btn">すべてみる</div>

<div class="abs contact-bg"></div>
<div class="abs contact-photo" role="img" aria-label="木材を加工する手元の写真"></div>
<div class="abs contact-panel">
  <h2>お問い合わせ</h2>
  <p class="en">Contact</p>
  <p class="tel">☎ 000-000-0000</p>
  <div class="btn">お問い合わせ</div>
</div>

<footer class="abs footer">
  <div class="footer-info"><strong>清瀬木工架装株式会社</strong><br>〒000-0000 ○○県○○市○○町0-0-0<br>TEL 000-000-0000 / FAX 000-000-0000</div>
  <nav class="footer-nav"><span>ホーム</span><span>業務内容</span><span>施工事例</span><span>会社概要</span><span>お問い合わせ</span></nav>
</footer>
<div class="abs pagetop"><svg width="24" height="24" viewBox="0 0 24 24"><path d="M8 14l4-4 4 4" fill="none" stroke="#fff" stroke-width="1.5"/></svg></div>
</body>
</html>
```